Webdesign für Bau von Wohnanlagen aus Containermodulen
Zielgruppe
Wir bauen Wohnanlagen, Bürogebäude, Kindergärten, Schulen etc. aus einzelnen Containermodulen - übernehmen die Montage, Umbau und Versetzung, Reparaturen und Einlagerungen. Unsere Zielgruppe sind überwiegend Firmen und Kommunen. Der Text für die Homepage ist bereits fertig. Hier erhalten Sie weitere Informationen über unser Tätigkeitsfeld.
Aufgabenstellung
Die Farbe unseres Logos ist blau. Sie sollte sich natürlich in der Homepage minimal widerspiegeln, aber nicht dominieren. Bilder sollten nicht zu klein gehalten werden. Wir möchten dadurch zeigen, was möglich ist (z.B. Umsetzungen von ganzen Containeranlagen am Stück - hier haben wir eine Monopolstellung).

```html
<!DOCTYPE html>
<html lang="de">
<head>
<meta charset="utf-8">
<title>KESSLER Montagebau – Aktuelles</title>
<link href="https://fonts.googleapis.com/css2?family=Open+Sans:wght@400;600;700&family=Roboto+Slab:wght@300&display=swap" rel="stylesheet">
<style>
  :root {
    --brand: #0f238f;
    --text: #4a4a4a;
    --muted: #333333;
    --footer: #5e5e5e;
    --light: #ebebeb;
    --white: #ffffff;
  }
  * { margin: 0; padding: 0; box-sizing: border-box; }
  html, body { width: 816px; height: 1200px; overflow: hidden; background: var(--white); }
  body { position: relative; font-family: "Open Sans", Arial, sans-serif; color: var(--text); }

  .site-header { position: absolute; top: 0; left: 0; width: 816px; height: 64px; }
  .brand {
    position: absolute; left: 158px; top: 12px; width: 116px; height: 43px;
    display: flex; align-items: center; gap: 5px;
  }
  .brand-square { width: 12px; height: 12px; background: var(--brand); flex: none; }
  .brand-name { font-weight: 700; font-size: 10.5px; color: var(--brand); letter-spacing: 0.3px; line-height: 1.1; }
  .tagline {
    position: absolute; left: 286px; top: 10px;
    font-family: "Roboto Slab", Georgia, serif; font-weight: 300; font-size: 11.4px; color: var(--muted);
  }
  .main-nav { position: absolute; top: 49px; left: 350px; width: 310px; height: 10px; }
  .main-nav a {
    position: absolute; top: 0; font-size: 6.8px; color: var(--muted); text-decoration: none; white-space: nowrap;
  }
  .main-nav a.active { color: var(--brand); font-weight: 700; }

  .hero {
    position: absolute; top: 64px; left: 0; width: 816px; height: 209px;
    background: linear-gradient(180deg, #d9ddd6 0%, #cfd3cc 18%, #e0622e 40%, #d8402e 62%, #2f5ca8 72%, #e76a2b 80%, #8a9a6a 88%, #d6d2c8 100%);
  }

  .breadcrumb {
    position: absolute; top: 280px; left: 159px; font-size: 6.2px; color: var(--muted); white-space: nowrap;
  }
  .breadcrumb .home { letter-spacing: 1.6px; }
  .breadcrumb .sep { margin: 0 3px; }

  .news-list { position: absolute; top: 307px; left: 158px; width: 502px; }
  .news-item { position: relative; height: 145px; margin-bottom: 17px; }
  .news-card { position: absolute; left: 0; top: 0; width: 158px; height: 145px; }
  .news-photo { width: 158px; height: 110px; }
  .news-headline {
    height: 35px; background: var(--brand); color: var(--white);
    font-weight: 600; font-size: 7.4px; line-height: 12.8px; padding: 5px 6px 0 8.5px; text-transform: uppercase;
  }
  .expand {
    position: absolute; right: 0; top: 0; width: 17px; height: 17px; background: var(--brand);
  }
  .news-body { position: absolute; left: 170px; top: 0; width: 332px; }
  .news-date { font-size: 6.2px; font-weight: 700; color: var(--brand); margin-top: 0; line-height: 8px; }
  .news-body p { font-size: 7.7px; line-height: 12.9px; margin-top: 8px; color: var(--text); }
  .news-body p + p { margin-top: 12.9px; }

  .pagination { position: absolute; top: 1127px; left: 530px; width: 130px; height: 22px; }
  .page {
    position: absolute; top: 0; width: 21px; height: 22px; font-size: 7.8px; color: var(--muted);
    display: flex; align-items: center; justify-content: center;
  }
  .page.current { background: var(--brand); color: var(--white); }
  .page.next { background: var(--light); }

  .site-footer {
    position: absolute; left: 0; top: 1174px; width: 816px; height: 26px; background: var(--footer);
    color: var(--white); font-size: 6.2px; letter-spacing: 1.3px; padding: 8px 0 0 155px; white-space: nowrap;
  }
  .site-footer span { margin-right: 6px; }
</style>
</head>
<body>
  <header class="site-header">
    <div class="brand"><span class="brand-square"></span><span class="brand-name">KESSLER MONTAGEBAU</span></div>
    <div class="tagline">Ihr Partner für mobile Container</div>
    <nav class="main-nav">
      <a style="left:0">HOME</a>
      <a style="left:38px">LEISTUNGEN</a>
      <a style="left:97px">WIR ÜBER UNS</a>
      <a style="left:164px">REFERENZEN</a>
      <a class="active" style="left:223px">AKTUELLES</a>
      <a style="left:279px">KONTAKT</a>
    </nav>
  </header>

  <div class="hero" role="img" aria-label="Foto einer mehrstöckigen Wohnanlage aus bunten Containermodulen"></div>

  <div class="breadcrumb"><span class="home">KESSLER MONTAGEBAU</span><span class="sep">»</span>Aktuelles</div>

  <main class="news-list">
    <article class="news-item">
      <div class="news-card">
        <div class="news-photo" role="img" aria-label="Foto: Kran hebt Containermodul unter einer Bühnenüberdachung" style="background:linear-gradient(180deg,#c9d6e6 0%,#e9edf1 35%,#5d8a3a 60%,#8c8c8c 100%)"></div>
        <div class="news-headline">Hier steht die Headline , Maecenas tempus tellus.</div>
      </div>
      <div class="news-body">
        <div class="news-date">25. November 2017</div>
        <p>Lorem ipsum dolor sit amet, consectetuer adipiscing elit. Aenean commodo ligula eget<br>dolor. Aenean massa. Cum sociis natoque penatibus et magnis dis parturient montes, nas-<br>cetur ridiculus mus.</p>
        <p>Donec quam felis, ultricies nec, pellentesque eu, pretium quis, sem. Nulla consequat massa<br>quis enim. Donec pede justo, fringilla vel, aliquet nec, vulputate eget, arcu. In enim justo,<br>rhoncus ut, imperdiet a, venenatis vitae, justo.</p>
        <p>Nullam dictum felis eu pede mollis pretium.</p>
      </div>
    </article>

    <article class="news-item">
      <div class="news-card">
        <div class="news-photo" role="img" aria-label="Foto: Mobilkran versetzt ein ganzes Containermodul" style="background:linear-gradient(180deg,#d6e0ec 0%,#b9bfc6 40%,#a9aeb3 60%,#6b5a52 85%,#8a8a86 100%)"></div>
        <div class="news-headline">Hier steht die Headline , Maecenas tempus tellus.</div>
        <svg class="expand" viewBox="0 0 17 17" aria-hidden="true"><path d="M8.5 4.5v8M4.5 8.5h8" stroke="#fff" stroke-width="1.6"/></svg>
      </div>
      <div class="news-body">
        <div class="news-date">22. November 2017</div>
        <p>Lorem ipsum dolor sit amet, consectetuer adipiscing elit. Aenean commodo ligula eget<br>dolor. Aenean massa. Cum sociis natoque penatibus et magnis dis parturient montes, nas-<br>cetur ridiculus mus.</p>
        <p>Donec quam felis, ultricies nec, pellentesque eu, pretium quis, sem. Nulla consequat massa<br>quis enim. Donec pede justo, fringilla vel, aliquet nec, vulputate eget, arcu. In enim justo,<br>rhoncus ut, imperdiet a, venenatis vitae, justo.</p>
        <p>Nullam dictum felis eu pede mollis pretium.</p>
      </div>
    </article>

    <article class="news-item">
      <div class="news-card">
        <div class="news-photo" role="img" aria-label="Foto: Bauarbeiter mit Helmen und Warnwesten besprechen Baupläne" style="background:linear-gradient(180deg,#cfc8bd 0%,#d8d04a 45%,#b9a76e 70%,#e8e6e1 100%)"></div>
        <div class="news-headline">Hier steht die Headline , Maecenas tempus tellus.</div>
      </div>
      <div class="news-body">
        <div class="news-date">16. November 2017</div>
        <p>Lorem ipsum dolor sit amet, consectetuer adipiscing elit. Aenean commodo ligula eget<br>dolor. Aenean massa. Cum sociis natoque penatibus et magnis dis parturient montes, nas-<br>cetur ridiculus mus.</p>
        <p>Donec quam felis, ultricies nec, pellentesque eu, pretium quis, sem. Nulla consequat massa<br>quis enim. Donec pede justo, fringilla vel, aliquet nec, vulputate eget, arcu. In enim justo,<br>rhoncus ut, imperdiet a, venenatis vitae, justo.</p>
        <p>Nullam dictum felis eu pede mollis pretium.</p>
      </div>
    </article>

    <article class="news-item">
      <div class="news-card">
        <div class="news-photo" role="img" aria-label="Foto: schwebendes graues Containermodul mit Fenstern" style="background:linear-gradient(180deg,#eef0f2 0%,#6f767c 40%,#4d5358 70%,#f1f2f3 100%)"></div>
        <div class="news-headline">Hier steht die Headline , Maecenas tempus tellus.</div>
      </div>
      <div class="news-body">
        <div class="news-date">07. Oktober 2017</div>
        <p>Lorem ipsum dolor sit amet, consectetuer adipiscing elit. Aenean commodo ligula eget<br>dolor. Aenean massa. Cum sociis natoque penatibus et magnis dis parturient montes, nas-<br>cetur ridiculus mus.</p>
        <p>Donec quam felis, ultricies nec, pellentesque eu, pretium quis, sem. Nulla consequat massa<br>quis enim. Donec pede justo, fringilla vel, aliquet nec, vulputate eget, arcu. In enim justo,<br>rhoncus ut, imperdiet a, venenatis vitae, justo.</p>
        <p>Nullam dictum felis eu pede mollis pretium.</p>
      </div>
    </article>

    <article class="news-item">
      <div class="news-card">
        <div class="news-photo" role="img" aria-label="Foto: Kranhaken mit Hebegurten über einem Containerdach" style="background:linear-gradient(180deg,#9fb7d4 0%,#d9e1ea 45%,#c8ccd2 75%,#6c7077 100%)"></div>
        <div class="news-headline">Hier steht die Headline , Maecenas tempus tellus.</div>
      </div>
      <div class="news-body">
        <div class="news-date">13. September 2017</div>
        <p>Lorem ipsum dolor sit amet, consectetuer adipiscing elit. Aenean commodo ligula eget<br>dolor. Aenean massa. Cum sociis natoque penatibus et magnis dis parturient montes, nas-<br>cetur ridiculus mus.</p>
        <p>Donec quam felis, ultricies nec, pellentesque eu, pretium quis, sem. Nulla consequat massa<br>quis enim. Donec pede justo, fringilla vel, aliquet nec, vulputate eget, arcu. In enim justo,<br>rhoncus ut, imperdiet a, venenatis vitae, justo.</p>
        <p>Nullam dictum felis eu pede mollis pretium.</p>
      </div>
    </article>
  </main>

  <nav class="pagination" aria-label="Seiten">
    <span class="page current" style="left:0">1</span>
    <span class="page" style="left:21px">2</span>
    <span class="page" style="left:42px">3</span>
    <span class="page" style="left:63px">4</span>
    <span class="page" style="left:84px">5</span>
    <span class="page next" style="left:107px">
      <svg width="7" height="7" viewBox="0 0 7 7" aria-hidden="true"><path d="M2.3 1l2.5 2.5L2.3 6" fill="none" stroke="#333" stroke-width="1"/></svg>
    </span>
  </nav>

  <footer class="site-footer"><span>KESSLER MONTAGEBAU</span><span>| © 2017</span><span>|</span><span>IMPRESSUM</span></footer>
</body>
</html>
```